Poster to inspire rural women around Australia!

We need a poster for our upcoming annual women's events in 2017. The poster will be used for every event this year (needs to be editable in Adobe suite of products) as a template sent to our event hosts around regional Australia. Our group will be hosting 3 events When the Doubters fall quiet / Can crafty neighbours lift each other? / Living with loss. We would like the design to be able to work across these 3 topics and to be clean, honest and use imagery which is meaningful for our target audience. Examples of previous posters attached.

Target Market(s)

'The Wanderers'; 30 - 60 year old women who live in regional Australia and have been removed from their normal conversations channels because of family (young or old).

Industry/Entity Type

Events

Font styles to use
Sans Serif

Colors
eda3c7
eaf2ce
f9d9e8
cadf82

Requirements
Must have
• A4 size poster
• Editable using Adobe products
• Organisation name - The Marrowbank Circle
• Event name, date, venue, time, booking details and price
Nice to have
• Our colours (themarrowbankcircle.com.au) green & pink
• tag line 'connecting women with conversation'

```html
<!DOCTYPE html>
<html lang="en">
<head>
<meta charset="utf-8">
<title>The Marrowbank Circle – Event Poster</title>
<link rel="stylesheet" href="https://fonts.googleapis.com/css2?family=Open+Sans:wght@300;400;800&family=Source+Sans+3:ital,wght@0,300;0,400;0,600;1,300&family=Fira+Sans+Condensed:wght@700&display=swap">
<style>
  :root {
    --pink: #eda3c7;
    --pale-green: #eaf2ce;
    --pale-pink: #f9d9e8;
    --green: #cadf82;
    --band-green: #c6de84;
    --ink: #555555;
    --text: #222222;
    --white: #ffffff;
  }
  * { box-sizing: border-box; margin: 0; padding: 0; }
  html, body { width: 848px; height: 1200px; overflow: hidden; background: var(--white); }
  .poster {
    position: relative; width: 848px; height: 1200px; overflow: hidden;
    font-family: "Source Sans 3", "Source Sans Pro", sans-serif; color: var(--text);
  }
  .landscape {
    position: absolute; left: 0; top: 470px; width: 848px; height: 730px;
    background: linear-gradient(180deg, #f3f4f4 0%, #e6ebe7 18%, #e4ead8 45%, #e9eed6 75%, #e3e8d8 100%);
  }
  .group-photo {
    position: absolute; left: 0; top: 0; width: 848px; height: 345px;
    background: linear-gradient(90deg, #8fa68a 0%, #b9b4a6 25%, #9e8c84 45%, #c9c3bb 65%, #b88f86 82%, #d8d3cc 100%);
  }
  .title-band {
    position: absolute; left: 0; top: 278px; width: 848px; height: 264px;
    background: var(--band-green);
    clip-path: polygon(0 62px, 100% 0, 100% 218px, 0 264px);
  }
  .band-rule {
    position: absolute; left: 0; top: 500px; width: 848px; height: 60px;
  }
  .masthead {
    position: absolute; left: 24px; top: 330px; width: 800px; text-align: center;
    transform: rotate(-4.2deg); color: var(--white);
  }
  .org-name {
    font-family: "Open Sans", sans-serif; font-weight: 800; font-size: 66px;
    line-height: 1; letter-spacing: -0.5px;
  }
  .tagline {
    font-family: "Open Sans", sans-serif; font-weight: 300; font-size: 36px;
    line-height: 1.1; margin-top: 2px; letter-spacing: 0.3px;
  }
  .event-time {
    position: absolute; left: 0; width: 848px; top: 530px; text-align: center;
    padding-left: 38px;
    font-family: "Fira Sans Condensed", sans-serif; font-weight: 700; font-size: 78px;
    line-height: 1; color: var(--ink);
  }
  .quote {
    position: absolute; left: 0; width: 848px; top: 606px; padding-left: 38px;
    text-align: center; font-style: italic; font-weight: 300; font-size: 19.5px; line-height: 27px; color: #333;
  }
  .intro {
    position: absolute; left: 0; width: 848px; top: 668px; padding-left: 8px;
    text-align: center; font-weight: 400; font-size: 20px; line-height: 27.3px; color: #1e1e1e;
  }
  .booking-panel {
    position: absolute; left: 94px; top: 906px; width: 660px; height: 186px;
    background: var(--pink); border-radius: 30px;
    box-shadow: 0 10px 14px rgba(0,0,0,0.22);
  }
  .booking-panel::before {
    content: ""; position: absolute; inset: 9px 11px 11px 16px;
    border: 2.5px solid var(--white); border-radius: 24px;
  }
  .booking-heading {
    position: absolute; left: 80px; top: 14px;
    font-weight: 600; font-size: 34px; letter-spacing: 0.5px; color: var(--ink);
  }
  .price-badge {
    position: absolute; left: 628px; top: 848px; width: 184px; height: 184px;
    filter: drop-shadow(2px 3px 3px rgba(0,0,0,0.25));
  }
  .price-label {
    position: absolute; left: 628px; top: 918px; width: 184px; text-align: center;
    font-weight: 400; font-size: 26px; color: var(--ink);
  }
  .website {
    position: absolute; left: 0; width: 848px; top: 1128px; padding-left: 8px; text-align: center;
    font-weight: 400; font-size: 37px; color: var(--ink); letter-spacing: 0.2px;
  }
</style>
</head>
<body>
<main class="poster">
  <div class="landscape" role="img" aria-label="Soft misty photograph of green rolling hills and bushland"></div>
  <div class="group-photo" role="img" aria-label="Photograph of a group of friends sharing tea outdoors in the countryside"></div>
  <div class="title-band"></div>
  <svg class="band-rule" viewBox="0 0 848 60" aria-hidden="true">
    <path d="M0 40 Q 420 10 848 6" fill="none" stroke="#d8d8d8" stroke-width="3"/>
  </svg>

  <header class="masthead">
    <h1 class="org-name">THE MARROWBANK CIRCLE</h1>
    <p class="tagline">CONNECTING WOMEN WITH CONVERSATION</p>
  </header>

  <h2 class="event-time">DATE-TIME</h2>

  <p class="quote">"Nothing compares to a beautiful conversation with a beautiful mind"<br>Mara Ellison</p>

  <p class="intro">
    The circle is for women in the wattlebrook area &amp; surrounds.<br>
    We host regular get togethers for women to connect, share &amp; learn about<br>
    our community, each other &amp; ourselves.<br>
    Our nights out are a relaxed way to meet with other women in the<br>
    community with wine &amp; food to keep your mind nourished and a few<br>
    beautiful Minds to arm you with a conversation starter.<br>
    Age is no barrier &amp; you never know who you might meet.
  </p>

  <section class="booking-panel">
    <h3 class="booking-heading">INFORMATION - BOOKINGS</h3>
  </section>

  <svg class="price-badge" viewBox="-92 -92 184 184" aria-hidden="true">
    <g fill="var(--green)">
      <circle id="petal" cx="58" cy="0" r="24"/>
      <use href="#petal" transform="rotate(30)"/>
      <use href="#petal" transform="rotate(60)"/>
      <use href="#petal" transform="rotate(90)"/>
      <use href="#petal" transform="rotate(120)"/>
      <use href="#petal" transform="rotate(150)"/>
      <use href="#petal" transform="rotate(180)"/>
      <use href="#petal" transform="rotate(210)"/>
      <use href="#petal" transform="rotate(240)"/>
      <use href="#petal" transform="rotate(270)"/>
      <use href="#petal" transform="rotate(300)"/>
      <use href="#petal" transform="rotate(330)"/>
      <circle cx="0" cy="0" r="62"/>
    </g>
  </svg>
  <p class="price-label">Price</p>

  <p class="website">themarrowbankcircle.com.au</p>
</main>
</body>
</html>
```